Business card design for a world class martial arts and group fitness facility

We need a professional and eye catching design for a business card. The card will be used in networking as well as marketing.
We are a martial arts facility offering Taekwondo, Brazilian Jiu Jitsu, and group fitness. All of our programs are geared for kids and adults.
Our Taekwondo program is lead by a Hall of Fame instructor who was Instructor of the Year in 2015.
Our Brazilian Jiu Jitsu program is lead by a wold class instructor who is also a part of the renown Brazilian KLO team.
We offer 3 focused group fitness programs: Ridge kickboxing, Tandem Fitness, and The Quarry which are all lead by certified instructors in a small group setting.
Our facility is state of the art and has been recognized as such in nationally published magazines.
Our business is named The Forge which is the linear logo that is attached. This is the main logo. I also attached a circular logo we have used in some marketing material. Our Jiu Jitsu program is the KLO team logo. The Taekwondo program is the VORTEN Prime. It would be nice to somehow incorporate all 3 logos, but The Forge is most important.
We would like to use all 3 logos if possible but The Forge is the most important. We would like to have a place for a staff member's name while keeping the focus on the programs we offer.

```html
<!DOCTYPE html>
<html lang="en">
<head>
<meta charset="utf-8">
<title>The Forge – Business Card</title>
<link rel="stylesheet" href="https://fonts.googleapis.com/css2?family=Open+Sans:wght@400;600;800&display=swap">
<style>
  :root {
    --stage: #e9e6e2;
    --card-white: #ffffff;
    --card-dark: #3b3b3b;
    --swoosh: #8a8a8a;
    --ink: #2a2a2a;
    --ink-soft: #555555;
    --mark-black: #111111;
    --mark-red: #c8202a;
    --mark-navy: #101a33;
  }
  html, body {
    margin: 0;
    padding: 0;
    overflow: hidden;
  }
  body {
    width: 1200px;
    height: 900px;
    background: var(--stage);
    font-family: "Open Sans", Arial, sans-serif;
    color: var(--ink);
    position: relative;
  }
  .card {
    position: absolute;
    left: 320px;
    width: 560px;
    height: 320px;
    box-shadow: 0 10px 28px rgba(0,0,0,0.22);
    overflow: hidden;
  }
  /* Front side */
  .card-front {
    top: 100px;
    background: var(--card-white);
  }
  .front-mark {
    position: absolute;
    display: flex;
    align-items: center;
    gap: 12px;
  }
  .mark-name {
    font-weight: 800;
    color: var(--ink);
    letter-spacing: 0.02em;
    white-space: nowrap;
  }
  .mark-dot {
    display: block;
    flex: none;
  }
  .front-team {
    left: 36px;
    top: 190px;
  }
  .front-team .mark-dot {
    width: 64px;
    height: 64px;
    border-radius: 50%;
    background: var(--mark-black);
  }
  .front-team .mark-name { font-size: 26px; }
  .front-main {
    left: 175px;
    top: 118px;
  }
  .front-main .mark-dot {
    width: 86px;
    height: 86px;
    border-radius: 50%;
    background: var(--ink-soft);
  }
  .front-main .mark-name { font-size: 34px; }
  .front-program {
    right: 30px;
    top: 34px;
    flex-direction: column;
    gap: 6px;
    align-items: center;
  }
  .front-program .mark-dot {
    width: 62px;
    height: 62px;
    background: var(--mark-navy);
  }
  .front-program .mark-name { font-size: 16px; }

  /* Back side */
  .card-back {
    top: 480px;
    background: var(--card-dark);
  }
  .card-back svg.back-shape {
    position: absolute;
    inset: 0;
  }
  .back-logo {
    position: absolute;
    left: 250px;
    top: 40px;
    display: flex;
    align-items: center;
    gap: 12px;
  }
  .back-logo .mark-dot {
    width: 70px;
    height: 70px;
    border-radius: 50%;
    background: var(--ink-soft);
  }
  .back-logo .mark-name { font-size: 32px; }
  .staff {
    position: absolute;
    left: 56px;
    top: 148px;
  }
  .staff-name {
    margin: 0;
    font-size: 19px;
    font-weight: 600;
    color: var(--ink);
  }
  .staff-role {
    margin: 0;
    font-size: 15px;
    color: var(--ink-soft);
  }
  .contact {
    position: absolute;
    left: 44px;
    top: 222px;
    list-style: none;
    margin: 0;
    padding: 0;
    font-size: 15px;
    color: var(--ink);
  }
  .contact li {
    display: flex;
    align-items: center;
    gap: 10px;
    height: 26px;
  }
  .contact svg { width: 14px; height: 14px; flex: none; }
</style>
</head>
<body>

  <section class="card card-front" aria-label="Card front">
    <div class="front-mark front-team">
      <span class="mark-dot"></span>
      <span class="mark-name">KLO</span>
    </div>
    <div class="front-mark front-main">
      <span class="mark-dot"></span>
      <span class="mark-name">THE FORGE</span>
    </div>
    <div class="front-mark front-program">
      <span class="mark-dot"></span>
      <span class="mark-name">VORTEN Prime</span>
    </div>
  </section>

  <section class="card card-back" aria-label="Card back">
    <svg class="back-shape" viewBox="0 0 560 320" width="560" height="320" aria-hidden="true">
      <ellipse cx="258" cy="196" rx="330" ry="170" fill="#ffffff"/>
      <path d="M -10 120 Q 60 20 250 12" fill="none" stroke="#8a8a8a" stroke-width="6"/>
      <path d="M -10 140 Q 70 40 240 26" fill="none" stroke="#bdbdbd" stroke-width="3"/>
      <path d="M 330 322 Q 520 300 575 190" fill="none" stroke="#8a8a8a" stroke-width="6"/>
      <path d="M 310 330 Q 510 312 570 215" fill="none" stroke="#bdbdbd" stroke-width="3"/>
    </svg>

    <div class="front-mark back-logo">
      <span class="mark-dot"></span>
      <span class="mark-name">THE FORGE</span>
    </div>

    <div class="staff">
      <p class="staff-name">Add Name</p>
      <p class="staff-role">Manager</p>
    </div>

    <ul class="contact">
      <li>
        <svg viewBox="0 0 24 24"><path d="M6.6 10.8a15 15 0 0 0 6.6 6.6l2.2-2.2a1 1 0 0 1 1-.25 11.4 11.4 0 0 0 3.6.57 1 1 0 0 1 1 1V20a1 1 0 0 1-1 1A17 17 0 0 1 3 4a1 1 0 0 1 1-1h3.5a1 1 0 0 1 1 1c0 1.25.2 2.45.57 3.57a1 1 0 0 1-.25 1z" fill="#2a2a2a"/></svg>
        123 456 7890
      </li>
      <li>
        <svg viewBox="0 0 24 24"><circle cx="12" cy="12" r="9.5" fill="none" stroke="#2a2a2a" stroke-width="2"/><ellipse cx="12" cy="12" rx="4" ry="9.5" fill="none" stroke="#2a2a2a" stroke-width="2"/><path d="M2.5 12h19" stroke="#2a2a2a" stroke-width="2"/></svg>
        www.danaholt.com
      </li>
      <li>
        <svg viewBox="0 0 24 24"><circle cx="12" cy="12" r="4" fill="none" stroke="#2a2a2a" stroke-width="2.2"/><path d="M16 8v5.5a2.5 2.5 0 0 0 5 0V12a9 9 0 1 0-3.5 7.1" fill="none" stroke="#2a2a2a" stroke-width="2.2"/></svg>
        danaholt@mailpost.com
      </li>
    </ul>
  </section>

</body>
</html>
```